Organic rose water based skincare line in need of product label and packaging design

We are looking for a simple, clean, modern labeling and packaging design for 2 of our products. Our brand's demographic is upscale females ages 20-40. We want our packaging to be very minimalistic, and instagramable.

Product #1: Rose water facial spray "Lumi Mist"
Product #2: Rose water facial toner "Velvet Hush Hour"

Please see attached images for our current logo and label design. We have also added some images that inspire our branding.

Target Market(s)

trendy woman ages 20-40

Industry/Entity Type

Skin Care Product

Font styles to use
Serif
Sans Serif

Colors

Designer to choose only greyscale colors for use in the design.

Requirements
Must have
• Must have our logo, bottle size, product name on front and how to use and ingredient on the back. Please see project description and attached images for more information.
Should not have
• Too much going on or too many colors.

```html
<!DOCTYPE html>
<html lang="en">
<head>
<meta charset="utf-8">
<title>Lumi Mist — Box Front</title>
<link rel="stylesheet" href="https://fonts.googleapis.com/css2?family=Montserrat:wght@300&family=Arimo:wght@400&display=swap">
<style>
  :root {
    --page-bg: #f4f1f1;
    --panel-white: #ffffff;
    --panel-edge: #e6dfe0;
    --ink: #111111;
    --ink-soft: #3a3a3a;
    --art-tone: #ecebeb;
  }
  * { margin: 0; padding: 0; box-sizing: border-box; }
  html, body {
    width: 1200px;
    height: 1200px;
    overflow: hidden;
    background: var(--page-bg);
  }
  .canvas {
    width: 1200px;
    height: 1200px;
    display: flex;
    align-items: center;
    justify-content: center;
  }
  .box-front {
    position: relative;
    width: 420px;
    height: 1060px;
    background: var(--panel-white);
    border: 1px solid var(--panel-edge);
    display: flex;
    flex-direction: column;
    align-items: center;
  }
  .brand-name {
    margin-top: 120px;
    font-family: "Montserrat", Helvetica, sans-serif;
    font-weight: 300;
    font-size: 18px;
    line-height: 1;
    letter-spacing: 4px;
    color: var(--ink);
    text-align: center;
    white-space: nowrap;
  }
  .product-name {
    margin-top: 148px;
    font-family: "Montserrat", Helvetica, sans-serif;
    font-weight: 300;
    font-size: 58px;
    line-height: 1.12;
    letter-spacing: 3px;
    color: var(--ink);
    text-align: center;
    text-transform: uppercase;
  }
  .product-descriptor {
    margin-top: 28px;
    font-family: "Arimo", Arial, sans-serif;
    font-size: 19px;
    line-height: 1.25;
    color: var(--ink-soft);
    text-align: center;
  }
  .rose-artwork {
    margin-top: 70px;
    width: 190px;
    height: 360px;
    background: linear-gradient(180deg, var(--art-tone), #f6f6f6);
  }
  .bottle-size {
    position: absolute;
    bottom: 90px;
    left: 0;
    right: 0;
    font-family: "Arimo", Arial, sans-serif;
    font-size: 17px;
    letter-spacing: 1px;
    color: var(--ink-soft);
    text-align: center;
  }
</style>
</head>
<body>
  <main class="canvas">
    <section class="box-front">
      <div class="brand-name">the dew room</div>
      <h1 class="product-name">Lumi<br>Mist</h1>
      <p class="product-descriptor">organic rosewater<br>hydrating mist</p>
      <div class="rose-artwork" role="img" aria-label="Single-line drawing of a long-stemmed rose"></div>
      <p class="bottle-size">2 oz / 60 mL</p>
    </section>
  </main>
</body>
</html>
```